Thistlow PowerPoint Slide Deck

We have created a new company the provides workforce solutions for rural healthcare providers in the United States. We have a website located at: https://thistlowpartners.example. Now we need a PowerPoint template that Thistlow employees can use to support in-person and virtual presentations. We want the final PowerPoint template/master slides to be consistent thematically with the Thistlow website, with an emphasis on simplicity -- clean, subtle, professional, relatively stark and with a white background dominant. It should use the Thistlow color scheme, logo and logo pattern. The product we select will need a cover/title slide as well as templates for a variety of slide layouts. Please refer to the Thistlow Style Guide attached to this request.

```html
<!DOCTYPE html>
<html lang="en">
<head>
<meta charset="utf-8">
<title>Thistlow Slide Templates</title>
<link href="https://fonts.googleapis.com/css2?family=Montserrat:wght@400;500;600;700&display=swap" rel="stylesheet">
<style>
  :root {
    --red: #e3191b;
    --red-deep: #b80f12;
    --ink: #141414;
    --paper: #f7f7f7;
    --white: #ffffff;
    --rule: #d4d4d4;
    --stage: #e6e6e6;
    --photo-a: #8fa3b8;
    --photo-b: #d9dfe6;
  }
  * { box-sizing: border-box; margin: 0; padding: 0; }
  html, body { width: 1200px; height: 714px; overflow: hidden; }
  body {
    background: var(--stage);
    font-family: "Montserrat", sans-serif;
    color: var(--ink);
    position: relative;
  }
  .slide {
    position: absolute;
    width: 560px; height: 315px;
    background: var(--paper);
    overflow: hidden;
    box-shadow: 0 6px 18px rgba(0,0,0,.12);
  }
  .slide > * { position: absolute; }
  .photo { background: linear-gradient(135deg, var(--photo-a), var(--photo-b)); }
  .pattern { background: linear-gradient(135deg, var(--red), #d9595b 50%, var(--red-deep)); }
  .brand { display: flex; align-items: center; gap: 6px; font-weight: 700; color: var(--ink); }
  .brand-mark { background: var(--red); display: block; }
  .accent { color: var(--red); }

  /* Cover: Tailored Solutions */
  .cover { left: 30px; top: 30px; }
  .cover .photo { left: 0; top: 0; width: 560px; height: 176px; }
  .cover .pattern { left: 0; top: 164px; width: 246px; height: 22px; }
  .cover .title { left: 34px; top: 200px; font-size: 22px; font-weight: 700; letter-spacing: -.2px; }
  .cover .lede { left: 36px; top: 234px; width: 440px; font-size: 10.5px; line-height: 1.38; }
  .cover .presenter { left: 34px; top: 285px; font-size: 10px; line-height: 1.1; }
  .cover .presenter b { font-weight: 700; }
  .cover .line { left: 183px; top: 291px; width: 210px; height: 1.5px; background: var(--ink); }
  .cover .brand { right: 18px; top: 280px; font-size: 21px; }
  .cover .brand-mark { width: 30px; height: 30px; }

  /* Title: Empowering */
  .title-slide { left: 610px; top: 30px; }
  .title-slide .red-block { left: 0; top: 0; width: 230px; height: 50px; background: var(--red); }
  .title-slide .pattern { left: 0; top: 0; width: 26px; height: 315px; }
  .title-slide .dark-block { left: 26px; top: 24px; width: 204px; height: 24px; background: #2a0608; }
  .title-slide .photo { left: 26px; top: 48px; width: 266px; height: 267px; }
  .title-slide .brand { right: 22px; top: 22px; font-size: 18px; }
  .title-slide .brand-mark { width: 26px; height: 26px; }
  .title-slide .title { left: 318px; top: 112px; font-size: 19px; font-weight: 700; line-height: 1.2; }
  .title-slide .presenter-box { left: 318px; top: 218px; background: var(--ink); color: var(--white); font-size: 9px; padding: 7px 10px; }
  .title-slide .presenter-box b { font-weight: 700; }
  .title-slide .date { left: 320px; top: 268px; font-size: 9.5px; font-weight: 600; }

  /* Agenda */
  .agenda { left: 320px; top: 369px; }
  .agenda .red-band { left: 0; top: 0; width: 282px; height: 44px; background: var(--red); }
  .agenda .pattern-side { left: 0; top: 10px; width: 30px; height: 120px; }
  .agenda .pattern-foot { left: 215px; top: 293px; width: 80px; height: 22px; }
  .agenda .subtitle { left: 50px; top: 66px; font-size: 10px; font-weight: 600; color: var(--red); letter-spacing: .2px; }
  .agenda .title { left: 50px; top: 82px; font-size: 22px; font-weight: 700; }
  .agenda .items { left: 50px; top: 126px; width: 280px; list-style: none; }
  .agenda .items li { font-size: 9.5px; font-weight: 500; padding: 13px 0 9px; border-bottom: 1px solid var(--rule); }
  .agenda .photo { left: 334px; top: 20px; width: 226px; height: 295px; }
  .agenda .brand { right: 16px; top: 16px; font-size: 15px; }
  .agenda .brand-mark { width: 22px; height: 22px; }
</style>
</head>
<body>

<section class="slide cover">
  <div class="photo" role="img" aria-label="Photo of smiling healthcare workers in a seminar, one raising a hand"></div>
  <div class="pattern" role="img" aria-label="Red and white triangle brand pattern band"></div>
  <h1 class="title">Tailored Solutions for <span class="accent">Rural Hospitals</span></h1>
  <p class="lede">At Thistlow, we’re dedicated to supporting rural hospitals and healthcare providers with personalized insurance, retirement, and workforce solutions—<span class="accent">helping you care for your teams as much as you care for your patients.</span></p>
  <p class="presenter"><b>Presented By Jane Doe</b><br>October 30th, 2025</p>
  <div class="line"></div>
  <div class="brand"><span class="brand-mark"></span>Thistlow</div>
</section>

<section class="slide title-slide">
  <div class="red-block"></div>
  <div class="dark-block"></div>
  <div class="pattern" role="img" aria-label="Red and white triangle brand pattern strip"></div>
  <div class="photo" role="img" aria-label="Portrait of a businesswoman with arms crossed in front of medical staff"></div>
  <div class="brand"><span class="brand-mark"></span>Thistlow</div>
  <h1 class="title">Empowering<br>Rural Healthcare<br>Organizations with<br><span class="accent">Tailored Solutions</span></h1>
  <p class="presenter-box">Presented By <b>Jane Doe</b></p>
  <p class="date">October 30th, 2025</p>
</section>

<section class="slide agenda">
  <div class="red-band"></div>
  <div class="pattern pattern-side" role="img" aria-label="Red and white triangle brand pattern strip"></div>
  <p class="subtitle">SUBTITLE GOES HERE</p>
  <h2 class="title">Our Agenda</h2>
  <ul class="items">
    <li>Lorem ipsum dolor sit amet consectetur</li>
    <li>Lorem ipsum dolor sit amet consectetur</li>
    <li>Lorem ipsum dolor sit amet consectetur</li>
    <li>Lorem ipsum dolor sit amet consectetur</li>
  </ul>
  <div class="pattern pattern-foot" role="img" aria-label="Red and white triangle brand pattern block"></div>
  <div class="photo" role="img" aria-label="Photo of a smiling doctor with stethoscope holding a blue folder"></div>
  <div class="brand"><span class="brand-mark"></span>Thistlow</div>
</section>

</body>
</html>
```